Hong Kong residential leasing and sales company needs a website design

Hong Kong has many competitive real estate agents. The majority of us have the same listings so, besides the team and experience, a website is what makes us stand out. A first impression. We need our website to be user friendly, informative and to have a wow factor. Most sites are generic so whilst we are close to accepting that maybe that's the only formula which works....we would like to see if we're missing something! Our clients are a mix of International users of all ages but probably ultimately 35+.. We have a logo (attached) which we would like to keep - designed by artmarketly. Flexible with colours except red.
examples of our competitors are:
http://www.brindlewoodestates.example
http://www.nuvo.example/home
http://www.premierdwellingsvx.example
http://www.orchid-lettings.example
http://www.tidemark-harrowgates.example
We were thinking of having the following in a menu bar with drop downs for most...some more than others. Home / For Sale / For Rent / Property 101 / About us / Contact Us ..
Look forward to seeing your ideas. Thanks in advance.

```html
<!DOCTYPE html>
<html lang="en">
<head>
<meta charset="utf-8">
<title>Harbourline Homes – Hong Kong Residential Sales &amp; Leasing</title>
<link rel="stylesheet" href="https://fonts.googleapis.com/css2?family=Cinzel:wght@400;600&family=Open+Sans:wght@400;600;700&display=swap">
<style>
:root{
  --purple:#58306f;
  --purple-light:#8a4fa8;
  --purple-mid:#6e3f8c;
  --text:#333;
  --muted:#777;
  --card:#f1f1f1;
  --yellow:#f6c22c;
  --line:#d6d6d6;
}
*{margin:0;padding:0;box-sizing:border-box}
html,body{width:674px;height:1200px;overflow:hidden}
body{position:relative;font-family:"Open Sans",sans-serif;color:var(--text);
  background:linear-gradient(180deg,#c9d6e2 0%,#aebfcf 30%,#d9dee3 45%,#eceff1 60%,#f2f3f4 100%)}
.abs{position:absolute}
.city-backdrop{position:absolute;inset:0 0 auto 0;height:460px;
  background:linear-gradient(180deg,#dbe5ee 0%,#9fb0c2 35%,#b7c3cd 60%,rgba(236,239,241,0) 100%)}
.page{position:absolute;left:110px;top:0;width:454px;height:1200px;background:#fff}
.brand{left:22px;top:22px;display:flex;align-items:center;gap:6px;font-family:"Cinzel",serif;font-size:13px;font-weight:600;color:var(--purple);letter-spacing:1px}
.brand .mark{width:12px;height:12px;background:var(--purple)}
.topbar{right:12px;top:23px;display:flex;align-items:center;gap:6px;font-size:7.5px;font-weight:700;font-style:italic;color:#444}
.topbar svg{display:block}
.lang,.search{top:40px;height:16px;border:1px solid var(--line);font-size:6.5px;color:#999;display:flex;align-items:center;padding:0 5px}
.lang{left:247px;width:65px;gap:4px}
.lang .flag{width:8px;height:5px;background:#7a8db8}
.search{left:316px;width:126px;justify-content:space-between}
.nav{left:11px;top:72px;width:431px;height:26px;background:var(--purple);display:flex}
.nav a{font-family:"Cinzel",serif;font-size:8.5px;color:#fff;text-decoration:none;display:flex;align-items:center;justify-content:center;gap:3px;border-right:1px solid #4a275e}
.nav a.active{background:var(--purple-light)}
.nav .dot{width:4px;height:4px;border-radius:50%;background:#fff}
.hero{left:11px;top:100px;width:431px;height:201px;background:linear-gradient(135deg,#7b6a55 0%,#b9a17d 35%,#e3d7c2 55%,#8a7860 80%,#4d3f33 100%)}
.quick-tab{left:32px;top:20px;width:18px;height:52px;background:var(--purple);color:#fff;font-size:6px;font-weight:600;writing-mode:vertical-rl;transform:rotate(180deg);display:flex;align-items:center;justify-content:center}
.quick{left:50px;top:20px;width:127px;height:156px;background:#fff}
.tab{top:0;height:22px;width:63px;font-size:10px;display:flex;align-items:center;justify-content:center}
.tab.rent{left:0;color:var(--purple)}
.tab.rent span{border-bottom:1px solid var(--purple)}
.tab.buy{left:64px;background:#9a9a9a;color:#fff}
.field{left:14px;height:15px;border:1px solid var(--line);font-size:6.5px;color:#999;display:flex;align-items:center;justify-content:space-between;padding:0 5px}
.field .caret{width:0;height:0;border-left:2px solid transparent;border-right:2px solid transparent;border-top:3px solid #999}
.btn{left:14px;top:117px;width:102px;height:20px;background:var(--yellow);color:#7a5a00;font-size:7px;font-weight:700;display:flex;align-items:center;justify-content:center}
.hero-cap{left:308px;top:137px;width:123px;height:37px;background:rgba(40,34,28,.6);color:#fff;font-size:8.5px;line-height:12px;padding:6px 11px}
.arrow{top:81px;width:17px;height:17px;border-radius:50%;background:#fff;display:flex;align-items:center;justify-content:center}
.section-title{left:110px;width:234px;height:22px;background:radial-gradient(ellipse at center,#d8d8d8 0%,#e6e6e6 55%,rgba(255,255,255,0) 75%);font-family:"Cinzel",serif;font-size:10px;color:#444;display:flex;align-items:center;justify-content:center;letter-spacing:.5px}
.intro{font-size:6.8px;line-height:10.4px;text-align:center;color:#333}
.tile{top:412px;height:130px}
.tile .cap{position:absolute;left:0;right:0;bottom:0;height:20px;background:rgba(60,50,70,.55);color:#fff;font-size:9px;display:flex;align-items:center;justify-content:center}
.card{width:106px;height:164px;background:var(--card);box-shadow:0 3px 4px rgba(0,0,0,.08)}
.card .photo{height:94px;position:relative}
.card .ref{position:absolute;left:0;top:0;background:rgba(0,0,0,.55);color:#fff;font-size:5.5px;padding:1px 5px;width:62px}
.card.active{background:var(--purple-light);color:#fff}
.card.active .ref{background:var(--purple-light)}
.card h3{font-weight:400;font-size:8.5px;margin:12px 0 0 8px}
.card p{font-size:5.8px;line-height:10.3px;color:var(--muted);margin:3px 0 0 8px}
.card.active p{color:#f1e6f6}
.ph-a{background:linear-gradient(135deg,#8c8f94,#d9d4c9 55%,#5c5650)}
.ph-b{background:linear-gradient(135deg,#c9bda3,#efe8d8 55%,#7a6d58)}
.ph-c{background:linear-gradient(135deg,#5d5a45,#b8b09a 55%,#3f3a30)}
.ph-d{background:linear-gradient(135deg,#b5926a,#e0c9a5 55%,#6b5038)}
.footer{left:0;top:1008px;width:454px;height:192px;background:var(--purple);color:#fff}
.footer h4{position:absolute;top:30px;font-family:"Cinzel",serif;font-weight:400;font-size:7px;letter-spacing:.3px;padding-bottom:6px;border-bottom:1px solid #7a5592}
.footer ul{position:absolute;top:51px;list-style:none;font-size:5.8px}
.footer li{height:15.2px;line-height:15.2px;border-bottom:1px solid #6a4584;width:62px}
.footer li::before{content:"+ ";color:#c9b3d6}
.foot-call{left:32px;top:160px;display:flex;gap:4px;align-items:center;font-size:7.8px;font-weight:700;font-style:italic}
.copy{right:36px;top:160px;font-size:7.8px;font-style:italic}
</style>
</head>
<body>
<div class="city-backdrop" role="img" aria-label="Blurred Hong Kong skyline backdrop"></div>
<main class="page">
  <div class="abs brand"><span class="mark"></span>Harbourline Homes</div>
  <div class="abs topbar">
    <svg width="6" height="7"><rect width="6" height="7" rx="1" fill="#3b6cb3"/></svg>
    <svg width="7" height="7"><circle cx="3.5" cy="3.5" r="3.5" fill="#3aa3dc"/></svg>
    <svg width="9" height="6"><rect x=".5" y=".5" width="8" height="5" fill="none" stroke="#888"/><path d="M.5 .5l4 3 4-3" fill="none" stroke="#888"/></svg>
    <span>CALL +852 3100 4400</span>
  </div>
  <div class="abs lang"><span class="flag"></span>Language</div>
  <div class="abs search">Search<svg width="7" height="7"><circle cx="3" cy="3" r="2.2" fill="none" stroke="#999"/><path d="M4.6 4.6L6.6 6.6" stroke="#999"/></svg></div>

  <nav class="abs nav">
    <a style="width:55px">HOME</a>
    <a class="active" style="width:72px">FOR SALE <span class="dot"></span></a>
    <a style="width:72px">FOR RENT <span class="dot"></span></a>
    <a style="width:84px">PROPERTY 101</a>
    <a style="width:64px">ABOUT US</a>
    <a style="width:84px;border:0">CONTACT US</a>
  </nav>

  <section class="abs hero" role="img" aria-label="Luxury living room with cream sofas and harbour view">
    <div class="abs quick-tab">Quick Search</div>
    <div class="abs quick">
      <div class="abs tab rent"><span>Rent</span></div>
      <div class="abs tab buy">Buy</div>
      <div class="abs field" style="top:34px;width:102px">Location<span class="caret"></span></div>
      <div class="abs field" style="top:54px;width:102px">Size<span class="caret"></span></div>
      <div class="abs field" style="top:74px;width:47px">Price<span class="caret"></span></div>
      <div class="abs field" style="top:74px;left:69px;width:47px">Price<span class="caret"></span></div>
      <div class="abs field" style="top:94px;width:102px">Bedroom</div>
      <div class="abs btn">SEARCH PLEASE</div>
    </div>
    <div class="abs hero-cap">Lorem Ipsum Property<br>Hongkong, Lorem</div>
    <div class="abs arrow" style="left:-4px"><svg width="5" height="7"><path d="M4 1L1 3.5 4 6" fill="none" stroke="#999"/></svg></div>
    <div class="abs arrow" style="right:-4px"><svg width="5" height="7"><path d="M1 1L4 3.5 1 6" fill="none" stroke="#999"/></svg></div>
  </section>

  <h2 class="abs section-title" style="top:327px">WELCOME TO HARBOURLINE HOMES</h2>
  <p class="abs intro" style="left:48px;top:357px;width:357px">Lorem ipsum dolor sit amet, consectetur adipiscing elit. In fermentum dolor non augue pretium egestas. Donec sem eros, tincidunt at congue ut, posuere sit amet est. Vivamus scelerisque viverra odio sit amet laoreet. Ut nec neque non justo rutrum tempor lobortis eu ante. Aliquam sagittis, nibh quis commodo auctor</p>

  <div class="abs tile" style="left:44px;width:181px;background:linear-gradient(180deg,#6f8fc0 0%,#c5d3e4 45%,#e9e9e6 60%,#6b7f4e 100%)" role="img" aria-label="Modern white villa with garden">
    <div class="cap">Property of the weak</div>
  </div>
  <div class="abs tile" style="left:228px;width:182px;background:linear-gradient(135deg,#a9c6ee 0%,#e5e4d6 40%,#a9c6ee 75%,#9fbde8 100%)" role="img" aria-label="Map of Hong Kong with office location pin">
    <div class="cap">Find us on the area map</div>
  </div>

  <h2 class="abs section-title" style="top:571px">FEATURED PROPERTIES</h2>
  <p class="abs intro" style="left:70px;top:601px;width:314px">Lorem ipsum dolor sit amet, consectetur adipiscing elit. In fermentum dolor non augue pretium egestas. Donec sem eros, tincidunt at</p>

  <div class="abs card" style="left:11px;top:637px"><div class="photo ph-a" role="img" aria-label="Apartment living room with city view"><span class="ref">Ref. #: 29190</span></div><h3>Lorem Ipsum Villa</h3><p>SA1,710 sq ft / GA2,104 sq ft<br>3 bedrooms, 2 bathrooms<br>HK$ 40,000,000</p></div>
  <div class="abs card active" style="left:120px;top:637px"><div class="photo ph-b" role="img" aria-label="Bright lounge with cream sofas"><span class="ref">Ref. #: 29190</span></div><h3>Lorem Ipsum Villa</h3><p>SA1,710 sq ft / GA2,104 sq ft<br>3 bedrooms, 2 bathrooms<br>HK$46,000,000</p></div>
  <div class="abs card" style="left:228px;top:637px"><div class="photo ph-c" role="img" aria-label="Dining room with plants"><span class="ref">Ref. #: 29190</span></div><h3>Lorem Ipsum Villa</h3><p>SA1,710 sq ft / GA2,104 sq ft<br>3 bedrooms, 2 bathrooms<br>HK$ 40,000,000</p></div>
  <div class="abs card" style="left:336px;top:637px"><div class="photo ph-d" role="img" aria-label="Living room with stone fireplace"><span class="ref">Ref. #: 29190</span></div><h3>Lorem Ipsum Villa</h3><p>SA1,710 sq ft / GA2,104 sq ft<br>3 bedrooms, 2 bathrooms<br>HK$ 40,000,000</p></div>

  <div class="abs card" style="left:11px;top:816px"><div class="photo ph-a" role="img" aria-label="Apartment living room with city view"><span class="ref">Ref. #: 29190</span></div><h3>Lorem Ipsum Villa</h3><p>SA1,710 sq ft / GA2,104 sq ft<br>3 bedrooms, 2 bathrooms<br>HK$ 40,000,000</p></div>
  <div class="abs card" style="left:120px;top:816px"><div class="photo ph-b" role="img" aria-label="Bright lounge with cream sofas"><span class="ref">Ref. #: 29190</span></div><h3>Lorem Ipsum Villa</h3><p>SA1,710 sq ft / GA2,104 sq ft<br>3 bedrooms, 2 bathrooms<br>HK$ 40,000,000</p></div>
  <div class="abs card" style="left:228px;top:816px"><div class="photo ph-c" role="img" aria-label="Dining room with plants"><span class="ref">Ref. #: 29190</span></div><h3>Lorem Ipsum Villa</h3><p>SA1,710 sq ft / GA2,104 sq ft<br>3 bedrooms, 2 bathrooms<br>HK$ 40,000,000</p></div>
  <div class="abs card" style="left:336px;top:816px"><div class="photo ph-d" role="img" aria-label="Living room with stone fireplace"><span class="ref">Ref. #: 29190</span></div><h3>Lorem Ipsum Villa</h3><p>SA1,710 sq ft / GA2,104 sq ft<br>3 bedrooms, 2 bathrooms<br>HK$ 40,000,000</p></div>

  <footer class="abs footer">
    <h4 style="left:30px;width:62px">Harbourline Homes</h4>
    <ul style="left:30px"><li>Home</li><li>About</li><li>Services</li><li>For Sale</li><li>For Rent</li><li>Property 101</li></ul>
    <h4 style="left:114px;width:62px">Popular</h4>
    <ul style="left:114px"><li>Causeway Bay</li><li>Central</li><li>Chung Hom Kok</li><li>Deep Water Bay</li><li>Happy Valley</li><li>Headland Road</li></ul>
    <h4 style="left:199px;width:140px">Living in Hong Kong</h4>
    <ul style="left:199px"><li>Causeway Bay</li><li>Central</li><li>Chung Hom Kok</li><li>Deep Water Bay</li><li>Happy Valley</li><li>Headland Road</li></ul>
    <ul style="left:275px"><li>Causeway Bay</li><li>Central</li><li>Chung Hom Kok</li><li>Deep Water Bay</li><li>Happy Valley</li><li>Headland Road</li></ul>
    <h4 style="left:364px;width:62px">Our Services</h4>
    <ul style="left:364px"><li>Causeway Bay</li><li>Central</li><li>Chung Hom Kok</li><li>Deep Water Bay</li><li>Happy Valley</li><li>Headland Road</li></ul>
    <div class="abs foot-call">
      <svg width="5" height="7"><rect width="5" height="7" rx="1" fill="#fff"/></svg>
      <svg width="7" height="7"><circle cx="3.5" cy="3.5" r="3.5" fill="#fff"/></svg>
      <svg width="9" height="6"><rect width="9" height="6" fill="#fff"/><path d="M0 0l4.5 3.3L9 0" fill="none" stroke="#58306f"/></svg>
      <span>CALL +852 3100 4400</span>
    </div>
    <div class="abs copy">© 2014</div>
  </footer>
</main>
</body>
</html>
```